Home Page Redesign for Pet Website

Looking to redesign the home page of our WORDPRESS website which will be renamed The Critter Cover Handbook 2015.

Looking for clean design which communicates clarity.
Updates

This is for a Wordpress site.

Please note that the design MUST include the content which is shown in the table in the brief!

Hi Thanks for the designs so far. We have just updated the brief to provide more information and clarify a few issues. We have also now included a couple of layout suggestions. They are just suggestions but it should give you a better idea of what we are looking for. And we have just increased the budget for 1st place by £120. Please feel free to message me if you have any questions. Many thanks. Maud

Please note that the new brief is in a file dated 25 Jan!

Reason: We have extended the deadline so we can continue working with the designers who have submitted designs we like. If you have any new designs please submit them by the original deadline of 7.37pm this evening (GMT). We are planning to make our final decision by Friday this week.

Target Market(s)

UK pet owners. All ages but largest age group is 35-50.

Industry/Entity Type

Insurance

Requirements
Must have
• Three clear content groups - LEARN, RESEARCH, CAMPAIGN (see brief for more details).
Stock photos with dogs and cats
Use current colour scheme
Must work with existing inner pages.
Existing font.. but 1pt larger
See brief for more details
Should not have
• Logo
Content from Existing Page (except for footer content... and menu headings).

```html
<!DOCTYPE html>
<html lang="en">
<head>
<meta charset="utf-8">
<title>The Critter Cover Handbook 2015</title>
<link rel="stylesheet" href="https://fonts.googleapis.com/css2?family=Noto+Serif&family=Roboto+Condensed&family=Source+Sans+3:wght@400;600;700&display=swap">
<style>
:root{
  --hero-a:#c9542a;--hero-b:#e8845a;--hero-c:#f1a27d;
  --learn:#1f8fe3;--research:#5fb979;--campaign-a:#9c55dc;--campaign-b:#b567ef;
  --dark:#353535;--darker:#262626;--ink:#555;--white:#fff;
  --panel:rgba(25,25,25,.72);--bio:rgba(214,110,30,.85);
  --serif:"Noto Serif",Georgia,serif;--sans:"Source Sans 3",Arial,sans-serif;--cond:"Roboto Condensed",Arial,sans-serif;
}
*{box-sizing:border-box;margin:0;padding:0}
html,body{width:1200px;height:2582px;overflow:hidden}
body{font-family:var(--sans);color:var(--white);background:var(--white);position:relative}
ul{list-style:none}
.wrap{width:942px;margin:0 auto;position:relative}

/* hero */
.hero{height:549px;position:relative;overflow:hidden}
.hero-photo{position:absolute;inset:0;background:radial-gradient(ellipse at 75% 55%,var(--hero-c) 0%,var(--hero-b) 35%,var(--hero-a) 100%)}
.nav{position:absolute;top:16px;left:128px;right:129px;height:38px;display:flex;align-items:center}
.nav a{font-family:var(--cond);font-size:17px;color:var(--white);text-decoration:none;margin-right:22px;text-transform:uppercase}
.search{margin-left:auto;width:203px;height:38px;border:2px solid var(--white);display:flex;align-items:center;justify-content:space-between;padding:0 12px;font-size:13px}
.hero-title{position:absolute;left:128px;top:135px;font-family:var(--serif);font-size:47px;line-height:54px;font-weight:400}
.hero-sub{position:absolute;left:128px;top:265px;font-size:23px;line-height:30px}
.btn{display:inline-block;border:1.5px solid var(--white);color:var(--white);font-size:17px;font-weight:600;letter-spacing:.5px;text-decoration:none;padding:0 28px;line-height:43px}
.hero .btn{position:absolute;left:129px;top:358px}
.dots{position:absolute;top:509px;left:578px;display:flex;gap:6px}
.dots i{width:10px;height:10px;background:var(--white);transform:rotate(45deg);display:block}
.dots i.on{background:#5a3a2a}

/* content grid */
.grid{display:grid;grid-template-columns:471px 471px;grid-auto-rows:348px}
.photo{display:block}
.tile{padding:24px 22px}
.tile h2{font-family:var(--serif);font-weight:400;font-size:26px;margin-bottom:20px}
.learn{background:var(--learn)}
.learn .cols{display:grid;grid-template-columns:216px 200px;column-gap:4px}
.ticks li{display:flex;gap:10px;font-size:14.5px;font-weight:700;line-height:19px;margin-bottom:14px}
.ticks svg{flex:none;width:15px;height:15px;margin-top:2px}
.research{background:var(--research);padding-top:24px}
.research .ticks li{margin-bottom:16px}
.research .btn{margin-top:14px}
.campaign{background:linear-gradient(135deg,var(--campaign-a),var(--campaign-b))}
.campaign p{font-size:13.5px;font-weight:600;line-height:24px;margin-bottom:26px}

/* band */
.band{height:408px;position:relative;background:linear-gradient(180deg,#3d5a2a 0%,#6f7f45 45%,#7aa040 100%)}
.band .wrap{display:flex;padding-top:48px}
.box{width:314px;height:317px;padding:22px 27px}
.box h3{font-family:var(--serif);font-weight:400;font-size:18px;margin-bottom:28px;text-transform:uppercase}
.box p{font-size:13px;line-height:19px}
.pop,.disc{background:var(--panel)}
.bio{background:var(--bio);width:314px}
.pop .item{margin-bottom:19px}
.pop time{display:block;font-size:11px;font-style:italic;margin-top:5px}
.bio-photo{display:block;width:259px;height:112px;margin:-10px 0 18px;border:2px solid var(--white);background:linear-gradient(180deg,#7f8a82,#a5907a)}

/* footer */
.foot{background:var(--dark);height:397px}
.foot .wrap{display:flex;justify-content:space-between;padding-top:42px}
.col h3{font-family:var(--serif);font-weight:400;font-size:21px;text-transform:uppercase;margin-bottom:24px}
.col{width:292px}
.col:first-child{width:242px}
.ad{width:242px;height:244px;background:var(--white);display:flex;align-items:center;justify-content:center;text-align:center;color:#c8c8c8;font-weight:700;font-size:40px;line-height:56px}
.widget{width:292px;height:244px;background:var(--white);padding:17px}
.feed{border:1px solid #aab4c6;height:209px;padding:7px;color:#333;font-size:10px}
.feed-head{display:flex;gap:8px;align-items:flex-start;margin-bottom:6px}
.ava{width:36px;height:36px;background:#9a6b5a;flex:none}
.feed-name{color:#3b5998;font-weight:700;font-size:11px}
.chip{display:inline-block;background:#e4e6ea;border:1px solid #c5c9d0;padding:1px 6px;font-size:10px;font-weight:700;margin:4px 4px 0 0;color:#333}
.faces{display:grid;gap:5px;margin-top:6px}
.faces.six{grid-template-columns:repeat(6,1fr)}
.faces.five{grid-template-columns:repeat(5,1fr)}
.faces span{display:block;height:36px}
.faces em{display:block;font-style:normal;font-size:8px;color:#666;text-align:center;margin-top:2px;overflow:hidden;white-space:nowrap}
.feed-note{border-top:1px solid #ddd;margin-top:7px;padding-top:4px;font-size:9px}
.linkbar{background:var(--darker);height:57px;display:flex;justify-content:center;align-items:center;gap:24px}
.linkbar a,.legal a{color:var(--white);text-decoration:none;font-size:13px;text-transform:uppercase}
.social{height:66px;display:flex;justify-content:center;align-items:center;gap:10px;border-bottom:1px solid #e4e4e4}
.social span{width:32px;height:32px;border-radius:50%;background:#5a5a5a;display:block}
.legal{text-align:center;color:var(--ink);font-size:12.5px;line-height:21px;padding-top:16px}
.legal a{color:var(--ink);text-transform:none;font-size:12.5px}
</style>
</head>
<body>
<svg width="0" height="0" style="position:absolute"><symbol id="tick" viewBox="0 0 16 16"><path d="M2 8.5l4 4 8-9" fill="none" stroke="#fff" stroke-width="2.6" stroke-linecap="round" stroke-linejoin="round"/></symbol></svg>

<header class="hero">
  <div class="hero-photo" role="img" aria-label="Photo of a tabby cat and a Yorkshire terrier against an orange backdrop"></div>
  <nav class="nav">
    <a href="#">Home</a><a href="#">Pet Insurance Reviews</a><a href="#">Provide A-Z</a><a href="#">Pet Insurance Policies</a><a href="#">Surveys</a><a href="#">&#8801; More</a>
    <div class="search">Search here<svg width="14" height="14" viewBox="0 0 14 14"><circle cx="5.5" cy="5.5" r="4.3" fill="none" stroke="#fff" stroke-width="2"/><path d="M8.7 8.7l4 4" stroke="#fff" stroke-width="2.2"/></svg></div>
  </nav>
  <h1 class="hero-title">The Critter Cover<br>Handbook 2015</h1>
  <p class="hero-sub">Independent unbiased information for<br>fellow pet owners</p>
  <a class="btn" href="#">LEARN MORE</a>
  <div class="dots"><i></i><i class="on"></i><i></i></div>
</header>

<main class="wrap grid">
  <div class="photo" role="img" aria-label="Photo of a white terrier and a ginger kitten on grass" style="background:linear-gradient(180deg,#8fb7de 0%,#c9d8c0 45%,#5f8a38 100%)"></div>
  <section class="tile learn">
    <h2>Learn About Pet Insurance</h2>
    <div class="cols">
      <ul class="ticks">
        <li><svg><use href="#tick"/></svg>Introduction to Pet Insurance</li>
        <li><svg><use href="#tick"/></svg>Vet Fees Cover Types</li>
        <li><svg><use href="#tick"/></svg>What to Consider before Buying</li>
        <li><svg><use href="#tick"/></svg>Ten Popular Pet Insurance Providers</li>
        <li><svg><use href="#tick"/></svg>Confused by Pet Insurance: Start Here!</li>
      </ul>
      <ul class="ticks">
        <li><svg><use href="#tick"/></svg>Third Party Liability Insurance</li>
        <li><svg><use href="#tick"/></svg>Six Vet Fees Pet Insurance Companies Won't Pay!</li>
        <li><svg><use href="#tick"/></svg>Why Cheap Pet Insurance is Risky</li>
        <li><svg><use href="#tick"/></svg>Why Your Pets Vet History is Important</li>
      </ul>
    </div>
  </section>
  <section class="tile research">
    <h2>Research UK Pet Insurance Policies</h2>
    <ul class="ticks">
      <li><svg><use href="#tick"/></svg>Analysis, Customer Reviews and Full Details of All UK Policies</li>
      <li><svg><use href="#tick"/></svg>Search our database for policies matching your criteria</li>
      <li><svg><use href="#tick"/></svg>Compare claims experiences for pet insurance providers</li>
    </ul>
    <a class="btn" href="#">LEARN MORE</a>
  </section>
  <div class="photo" role="img" aria-label="Photo of a black and tan puppy playing with a tabby kitten on a white blanket" style="background:linear-gradient(180deg,#ecebe8 0%,#b89a78 50%,#e6e4e0 100%)"></div>
  <div class="photo" role="img" aria-label="Photo of a golden retriever nuzzling a white and brown cat on a lawn" style="background:linear-gradient(135deg,#6f7c4c 0%,#c49a62 55%,#8b8f5a 100%)"></div>
  <section class="tile campaign">
    <h2>Campaign For Fairer Pet Insurance</h2>
    <p>Lorem ipsum dolor sit amet, consectetur adipiscing elit. Vivamus fermentum, arcu ac luctus porta, lectus lorem fermentum lectus, vitae pretium elit quam eu libero. Curabitur tincidunt in libero finibus venenatis. Vivamus lacinia ac mauris et euismod. Ut sit amet facilisis dolor, et sodales augue. Quisque facilisis libero eget justo elementum pulvinar. Nam consectetur mauris et est finibus, nec ullamcorper nisl iaculis.</p>
    <a class="btn" href="#">LEARN MORE</a>
  </section>
</main>

<section class="band" role="img" aria-label="Soft blurred photo of pets in a garden">
  <div class="wrap">
    <div class="box pop">
      <h3>Popular Resources</h3>
      <div class="item"><p>Integer mattis neque quis tempus consectetur. Vestibulum elementum efficitur dapibus.</p><time>27-01-2015</time></div>
      <div class="item"><p>Integer mattis neque quis tempus consectetur. Vestibulum elementum efficitur dapibus.</p><time>27-01-2015</time></div>
      <div class="item"><p>Integer mattis neque quis tempus consectetur. Vestibulum elementum efficitur dapibus.</p><time>27-01-2015</time></div>
    </div>
    <div class="box bio">
      <h3>Bio</h3>
      <span class="bio-photo" role="img" aria-label="Photo of two dogs lying on a wooden deck"></span>
      <p>Integer mattis neque quis tempus consectetur. Vestibulum elementum efficitur dapibus. Morbi id egestas tortor, id convallis nunc. Vestibulum lobortis sit amet mi.</p>
    </div>
    <div class="box disc">
      <h3>Disclaimer</h3>
      <p>Please note that pet insurance terms often change. Whilst we will do our best to keep this website up to date you must check with the appropriate insurer before making any decisions. If you find any mistakes on this website please do let us know so we can correct it for the benefit of future visitors. Many thanks! -</p>
    </div>
  </div>
</section>

<footer>
  <div class="foot">
    <div class="wrap">
      <div class="col"><h3>Add Here</h3><div class="ad">AD<br>HERE</div></div>
      <div class="col"><h3>Join Us on Chatterbook</h3>
        <div class="widget"><div class="feed">
          <div class="feed-head"><span class="ava" role="img" aria-label="Profile photo"></span><div><div class="feed-name">Critter Cover Surveys UK</div><span class="chip">Like</span>You liked this.</div></div>
          <div>You and 2,122 others like <span class="feed-name" style="font-weight:400">Critter Cover Surveys UK</span></div>
          <div class="faces six" role="img" aria-label="Grid of follower profile photos">
            <span style="background:#8aa0b8"></span><span style="background:#c9a46a"></span><span style="background:#6f7f92"></span><span style="background:#b58a7a"></span><span style="background:#9fb0c2"></span><span style="background:#7a6a60"></span>
            <span style="background:#c48a6a"></span><span style="background:#d0a080"></span><span style="background:#8a7060"></span><span style="background:#a0a8b0"></span><span style="background:#b07050"></span><span style="background:#6a5a50"></span>
          </div>
          <div class="feed-note">Chatterbook social plugin</div>
        </div></div>
      </div>
      <div class="col"><h3>Latest From Chirper</h3>
        <div class="widget"><div class="feed">
          <div class="feed-head"><span class="ava" role="img" aria-label="Profile photo"></span><div><div class="feed-name">Critter Cover Surveys UK <span style="font-weight:400;color:#888">on Chirper</span></div><span class="chip">Follow</span></div></div>
          <div>1937 people follow Critter Cover Surveys UK</div>
          <div class="faces five" role="img" aria-label="Grid of follower profile photos">
            <div><span style="background:#5a6a9a"></span><em>PetPal</em></div><div><span style="background:#e0b020"></span><em>jenna</em></div><div><span style="background:#8a8a8a"></span><em>CatNap</em></div><div><span style="background:#4a90c0"></span><em>Orbit</em></div><div><span style="background:#9a8070"></span><em>pam</em></div>
            <div><span style="background:#a09080"></span><em>Brad</em></div><div><span style="background:#706050"></span><em>Jess</em></div><div><span style="background:#c02020"></span><em>heo</em></div><div><span style="background:#b09070"></span><em>Nino</em></div><div><span style="background:#605040"></span><em>duba</em></div>
          </div>
        </div></div>
      </div>
    </div>
  </div>
  <nav class="linkbar"><a href="#">About Us</a><a href="#">Legal Information &amp; Disclaimers</a><a href="#">Privacy Policy</a></nav>
  <div class="social"><span role="img" aria-label="Chatterbook"></span><span role="img" aria-label="Chirper"></span><span role="img" aria-label="Circle"></span></div>
  <div class="legal"><a href="#">About Us</a> | <a href="#">Legal Information &amp; Disclaimers</a> | <a href="#">Privacy Policy</a><br>copyright © 2015. Critter Cover Surveys UK. All Right Reserved</div>
</footer>
</body>
</html>
```